We want to design total new business card and logo for Kestrel Building Services Ltd

Our company name Kestrel Building Services Ltd. Design new logo and business card , need hi-end luxury style art for architecture and construction industry. The card should simple but stylish. Our business focus on CONNECT tradesman to construction company, help marketing construction company tender oversea projects, managing franchise in construction sector, delivery amazing services to our client, so Logo should show the CONNECTION IDEA, CONNECTING PEOPLE, LUXURY. Visit our website for more information: kestrelhub.co.nz

Low design quality

Target Market(s)

Directors or managers

Industry/Entity Type

Construction Company

Contact Information for Business Card

Name, Title, Mobile, Email, Website

Font styles to use
Serif

Colors

Designer to choose colors to be used in the design.

Requirements
Must have
• Simple and luxury, connection icon
Nice to have
• Special materials, plastic card, look through,...
• Look new ideas.

```html
<!DOCTYPE html>
<html lang="en">
<head>
<meta charset="utf-8">
<title>Kestrel Building Services – Business Card</title>
<link rel="stylesheet" href="https://fonts.googleapis.com/css2?family=Open+Sans:wght@400;600;700&display=swap">
<style>
  :root {
    --backdrop: #e8e8e6;
    --card-white: #fbfbfb;
    --brand-teal: #02a8c8;
    --ink-grey: #6b6b6b;
    --ink-white: #ffffff;
  }
  * { margin: 0; padding: 0; box-sizing: border-box; }
  html, body {
    width: 1200px;
    height: 900px;
    overflow: hidden;
    background: var(--backdrop);
    font-family: "Open Sans", Arial, sans-serif;
  }
  .business-card {
    position: absolute;
    left: 150px;
    top: 171px;
    width: 900px;
    height: 558px;
    display: flex;
    box-shadow: 0 10px 30px rgba(0,0,0,0.12);
  }
  .card-front {
    width: 455px;
    height: 100%;
    background: var(--card-white);
    position: relative;
  }
  .brand-mark {
    position: absolute;
    left: 0;
    right: 0;
    top: 198px;
    text-align: center;
  }
  .brand-square {
    display: block;
    width: 26px;
    height: 26px;
    margin: 0 auto 22px;
    background: var(--brand-teal);
  }
  .brand-name {
    color: var(--brand-teal);
    font-weight: 700;
    font-size: 30px;
    line-height: 1.1;
    letter-spacing: -0.3px;
    white-space: nowrap;
  }
  .brand-tagline {
    margin-top: 8px;
    color: var(--ink-grey);
    font-size: 18px;
    font-weight: 400;
    letter-spacing: 0.2px;
    white-space: nowrap;
  }
  .card-details {
    flex: 1;
    height: 100%;
    background: var(--brand-teal);
    color: var(--ink-white);
    position: relative;
  }
  .person {
    position: absolute;
    left: 42px;
    top: 62px;
  }
  .person-name {
    font-size: 30px;
    font-weight: 700;
    line-height: 1.1;
  }
  .person-title {
    font-size: 25px;
    font-weight: 400;
    line-height: 1.1;
  }
  .contact-list {
    position: absolute;
    left: 42px;
    top: 238px;
    list-style: none;
  }
  .contact-item {
    display: flex;
    align-items: center;
    font-size: 24px;
    line-height: 33px;
    white-space: nowrap;
  }
  .contact-icon {
    width: 18px;
    height: 18px;
    margin-right: 12px;
    fill: var(--ink-white);
    flex: none;
  }
  .company-address {
    position: absolute;
    left: 42px;
    top: 387px;
    font-style: normal;
    font-size: 24px;
    line-height: 33px;
    white-space: nowrap;
  }
</style>
</head>
<body>
  <div class="business-card">
    <section class="card-front">
      <div class="brand-mark">
        <span class="brand-square"></span>
        <div class="brand-name">KESTREL BUILDING SERVICES</div>
        <div class="brand-tagline">SOLID CRAFT HONEST FAIR PRICING</div>
      </div>
    </section>
    <section class="card-details">
      <div class="person">
        <div class="person-name">MARCUS HALE</div>
        <div class="person-title">Managing Director</div>
      </div>
      <ul class="contact-list">
        <li class="contact-item">
          <svg class="contact-icon" viewBox="0 0 20 20" aria-hidden="true"><path d="M2 7c0-2 3-4 8-4s8 2 8 4v2h-4V7.5c-1-.6-2.5-.9-4-.9s-3 .3-4 .9V9H2z"/><path d="M4 11l3-3h6l3 3v6H4z"/><circle cx="10" cy="13.5" r="1.8" fill="#02a8c8"/></svg>
          0800 555 014
        </li>
        <li class="contact-item">
          <svg class="contact-icon" viewBox="0 0 20 20" aria-hidden="true"><path d="M2 7c0-2 3-4 8-4s8 2 8 4v2h-4V7.5c-1-.6-2.5-.9-4-.9s-3 .3-4 .9V9H2z"/><path d="M4 11l3-3h6l3 3v6H4z"/><circle cx="10" cy="13.5" r="1.8" fill="#02a8c8"/></svg>
          021 555 0192
        </li>
        <li class="contact-item">
          <svg class="contact-icon" viewBox="0 0 20 20" aria-hidden="true"><rect x="2" y="5" width="16" height="11"/><path d="M2.5 5.5l7.5 6 7.5-6" fill="none" stroke="#02a8c8" stroke-width="1.4"/></svg>
          info@kestrelhub.co.nz
        </li>
        <li class="contact-item">
          <svg class="contact-icon" viewBox="0 0 20 20" aria-hidden="true"><circle cx="10" cy="10" r="8"/><path d="M2 10h16M10 2c-3 3-3 13 0 16M10 2c3 3 3 13 0 16" fill="none" stroke="#02a8c8" stroke-width="1.2"/></svg>
          www.kestrelhub.co.nz
        </li>
      </ul>
      <address class="company-address">
        KESTREL BUILDING SERVICES LTD<br>
        18 Totara Road, Manukau,<br>
        Auckland 2104, Newzealand
      </address>
    </section>
  </div>
</body>
</html>
```